Veltrane Management

We need a web design for a new consulting company, with clients all over the world. The company provides management consulting to the travel industry.

Logo files are attached.

Website must look very corporate and be responsive in design.

Management Consulting

```html
<!DOCTYPE html>
<html lang="en">
<head>
<meta charset="utf-8">
<title>Veltrane Management</title>
<link rel="stylesheet" href="https://fonts.googleapis.com/css2?family=Bree+Serif&family=Oxygen:wght@400;700&family=Roboto:wght@400&display=swap">
<style>
:root{
  --navy:#15264a;
  --blue:#1b6db3;
  --green:#7db544;
  --ring:#c8ccd4;
  --ring-green:#cfe3c3;
  --icon:#1e1e1e;
  --text:#333;
  --rule:#dcdcdc;
  --panel:#ececec;
  --footer-top:#3a3a3a;
  --footer-bottom:#1f1f1f;
  --white:#fff;
}
*{box-sizing:border-box;margin:0;padding:0}
html,body{width:882px;height:1200px;overflow:hidden}
body{position:relative;font-family:'Oxygen',sans-serif;color:var(--text);background:var(--white)}
a{color:inherit;text-decoration:none}
h1,h2,h3,h4{font-weight:400}

/* header */
.site-header{position:absolute;left:0;top:0;width:882px;height:78px;border-top:3px solid #888;background:linear-gradient(#fff,#eef0f2)}
.brand{position:absolute;display:flex;align-items:center;gap:8px;font-family:'Bree Serif',serif;color:var(--navy);white-space:nowrap}
.brand-mark{border-radius:50%;background:var(--blue);flex:none}
.site-header .brand{left:106px;top:21px;font-size:21px}
.site-header .brand-mark{width:38px;height:38px}
.phone{position:absolute;right:106px;top:14px;display:flex;align-items:center;gap:6px;font-size:15px;color:#222}
.main-nav{position:absolute;right:94px;top:45px;display:flex;font-size:11px;color:#222}
.main-nav a{padding:1px 11px;border-left:1px solid #bbb}
.main-nav a:first-child{border-left:0;color:var(--blue);text-decoration:underline}

/* hero */
.hero{position:absolute;left:0;top:78px;width:882px;height:328px;border-bottom:3px solid #2a2a2a;
  background:
    radial-gradient(ellipse 90px 70px at 540px 150px,rgba(214,180,160,.85),rgba(214,180,160,0)),
    radial-gradient(ellipse 140px 110px at 700px 150px,rgba(230,236,240,.35),rgba(230,236,240,0)),
    linear-gradient(90deg,#b7d0da 0%,#a7c4cf 38%,#7e99a5 50%,#2b3238 60%,#1f2429 78%,#303a42 88%,#23292e 100%)}
.hero-title{position:absolute;left:108px;top:59px;font-family:'Roboto',sans-serif;font-weight:400;font-size:20.5px;line-height:29px;color:var(--navy)}
.slider-arrow{position:absolute;width:28px;height:28px;border-radius:50%;background:#1e1e1e;border:2px solid #555;display:flex;align-items:center;justify-content:center}

/* about */
.about{position:absolute;left:0;top:406px;width:882px;height:130px;text-align:center}
.section-title{font-family:'Bree Serif',serif;font-size:19px;color:var(--navy);letter-spacing:.3px}
.section-title .accent{color:var(--blue)}
.about-title{position:absolute;left:0;width:882px;top:14px;display:flex;justify-content:center;align-items:center;gap:9px}
.about-title .brand{position:static;font-size:15px}
.about-title .brand-mark{width:26px;height:26px}
.about p{position:absolute;left:110px;width:662px;top:49px;font-size:10px;line-height:15.3px;color:#444}

/* services */
.services{position:absolute;left:0;top:536px;width:882px;height:197px;background:var(--panel);border-top:1px solid #ddd;border-bottom:1px solid #ddd}
.services .section-title{position:absolute;left:0;width:882px;top:16px;text-align:center}
.service{position:absolute;top:62px;width:150px;text-align:center;font-family:'Bree Serif',serif;font-size:11px;line-height:11.5px;color:#222}
.service-icon{display:block;width:78px;height:78px;margin:0 auto 18px}

/* columns */
.col{position:absolute;top:758px;width:208px}
.col-title{font-family:'Bree Serif',serif;font-size:15.5px;color:var(--navy);display:flex;align-items:center;gap:7px;padding-bottom:6px;border-bottom:2px solid var(--rule);white-space:nowrap}
.col-title .accent{color:var(--blue)}
.news-item{font-size:9px;line-height:12.5px;color:#333;padding:10px 0 7px;border-bottom:1px dashed #ccc}
.news-item:last-of-type{border-bottom:0}
.news-item b{font-size:10px;display:block}
.read-more{display:block;text-align:right;font-size:9px;font-weight:700;color:var(--blue)}
.quote{margin-top:12px;background:#e9e9e9;border-radius:8px;padding:10px 10px 22px 32px;font-size:9px;line-height:14.5px;font-style:italic;color:#444;position:relative}
.quote-mark{position:absolute;left:12px;top:10px;width:14px;height:10px;background:#c9c9c9;border-radius:3px}
.client{position:relative;display:flex;align-items:flex-end;gap:12px;margin-top:-20px;padding-left:14px;font-size:9.5px;color:#222}
.client-photo{width:48px;height:48px;border:2px solid #fff;box-shadow:0 0 0 1px #ccc;background:linear-gradient(#e4e8ec,#8592a0)}
.client-name{padding-bottom:10px}
.field{display:block;width:207px;height:21px;border:1px solid #bbb;border-radius:3px;margin-bottom:5px;font-size:9px;color:#777;font-style:italic;padding:5px 6px;background:#fff}
.field.message{height:53px}
.submit{display:inline-block;margin-top:6px;background:linear-gradient(#2168ad,#0e3f73);color:#fff;font-size:10.5px;font-weight:700;padding:3px 9px;border-radius:2px}

/* clients */
.clients{position:absolute;left:0;top:953px;width:882px;height:133px;background:var(--panel);border-top:1px solid #ddd}
.clients .section-title{position:absolute;left:0;width:882px;top:15px;text-align:center}
.client-logo{position:absolute;top:55px;height:55px;background:#fff;display:flex;align-items:center;justify-content:center;gap:6px;font-weight:700;font-size:15px;color:#2a2a2a;white-space:nowrap}
.client-logo i{width:12px;height:12px;background:#2a2a2a;display:block}

/* footer */
.site-footer{position:absolute;left:0;top:1086px;width:882px;height:114px;background:linear-gradient(var(--footer-top),var(--footer-bottom));border-top:2px solid #555;color:#ddd}
.footer-box{position:absolute;top:17px;height:57px;border:1px solid #5a5a5a;background:rgba(255,255,255,.06);padding:5px 8px}
.footer-box h4{font-size:10.5px;color:#fff;font-weight:700;margin-bottom:8px}
.newsletter-input{display:inline-block;width:132px;height:20px;background:#6a6a6a;border-radius:2px;font-size:9px;font-style:italic;color:#ddd;padding:4px 6px;vertical-align:middle}
.newsletter-go{display:inline-block;width:22px;height:20px;background:#5a5a5a;margin-left:4px;vertical-align:middle;text-align:center;line-height:20px}
.contact-line{display:flex;align-items:center;gap:7px;font-size:9px;line-height:14px}
.social{display:flex;gap:7px}
.social span{width:19px;height:19px;background:#2b6cb8}
.social span:nth-child(2){background:#2aa6dc}
.site-footer .brand{right:102px;top:28px;color:#fff;font-size:19px}
.site-footer .brand-mark{width:32px;height:32px;background:#fff}
.footer-links{position:absolute;left:105px;top:89px;font-size:9px;color:#ddd}
.footer-links a{padding:0 4px}
.footer-links a:first-child{padding-left:0}
.copyright{position:absolute;right:104px;top:89px;font-size:9px}
</style>
</head>
<body>

<header class="site-header">
  <a class="brand" href="#"><span class="brand-mark"></span>Veltrane Management</a>
  <div class="phone">
    <svg width="14" height="14" viewBox="0 0 14 14"><rect width="14" height="14" rx="2" fill="#1b6db3"/><path d="M4 3.5c.5-.3 1-.3 1.3.2l.7 1.3c.2.4 0 .7-.3 1l-.4.3c.4 1 1.2 1.8 2.2 2.2l.3-.4c.3-.3.6-.5 1-.3l1.3.7c.5.3.5.8.2 1.3-.6.8-1.5 1-2.4.6C6 9.6 4.4 8 3.6 6 3.2 5 3.4 4.1 4 3.5z" fill="#fff"/></svg>
    555 014 2290
  </div>
  <nav class="main-nav">
    <a href="#">Home</a><a href="#">About Us</a><a href="#">Services</a><a href="#">Contact Us</a>
  </nav>
</header>

<section class="hero" role="img" aria-label="Photo of a businessman in a dark suit sketching a white outline of an airplane, with line drawings of world landmarks on a pale blue background">
  <h1 class="hero-title">We Provides Management<br>Consulting to the<br>Travel Industry</h1>
  <span class="slider-arrow" style="left:74px;top:139px"><svg width="8" height="10" viewBox="0 0 8 10"><path d="M6 1 2 5l4 4" stroke="#fff" stroke-width="1.6" fill="none"/></svg></span>
  <span class="slider-arrow" style="left:782px;top:139px"><svg width="8" height="10" viewBox="0 0 8 10"><path d="M2 1l4 4-4 4" stroke="#fff" stroke-width="1.6" fill="none"/></svg></span>
</section>

<section class="about">
  <div class="about-title">
    <span class="section-title"><span class="accent">ABOUT</span></span>
    <span class="brand"><span class="brand-mark"></span>Veltrane Management</span>
  </div>
  <p>Lorem ipsum dolor sit amet, consectetuer adipiscing elit,Sed diam nonummy nibh euismod tincidunt ut laoreet dolore magna aliquam erat volutpat. Ut wisi enim ad minim veniam, quis nostrud exerci tation ullamcorper suscipit lobortis nisl ut aliquip &nbsp;commodo consequat. Duis autem vel eum iriure dolor in hendrerit in vulputate velit esse molestie consequat, vel ill dolore eu feugiat nulla facilisis at vero eros et accumsan et iusto odio dignissim qui blandit praesent luptatumdeelenit augue duis dolore te feugait nulla facilisi.</p>
</section>

<section class="services">
  <h2 class="section-title"><span class="accent">OUR</span> SERVICES</h2>

  <div class="service" style="left:93px">
    <svg class="service-icon" viewBox="0 0 78 78" aria-hidden="true">
      <circle cx="39" cy="39" r="33" fill="none" stroke="var(--ring)" stroke-width="9"/>
      <path d="M10 30A30 30 0 0 1 52 9" fill="none" stroke="var(--ring-green)" stroke-width="9"/>
      <rect x="18" y="46" width="7" height="14" fill="var(--icon)"/><rect x="28" y="40" width="7" height="20" fill="var(--icon)"/><rect x="38" y="34" width="7" height="26" fill="var(--icon)"/><rect x="48" y="28" width="7" height="32" fill="var(--icon)"/>
      <path d="M17 40 40 24l6 5 12-12" stroke="var(--icon)" stroke-width="3" fill="none"/><path d="M52 14h9v9z" fill="var(--icon)"/>
    </svg>SALES/<br>MARKETING</div>

  <div class="service" style="left:223px">
    <svg class="service-icon" viewBox="0 0 78 78" aria-hidden="true">
      <circle cx="39" cy="39" r="33" fill="none" stroke="var(--ring)" stroke-width="9"/>
      <path d="M10 30A30 30 0 0 1 52 9" fill="none" stroke="var(--ring-green)" stroke-width="9"/>
      <circle cx="34" cy="29" r="8" fill="var(--icon)"/><path d="M18 56c0-11 7-17 16-17s14 5 15 10v7z" fill="var(--icon)"/>
      <circle cx="51" cy="52" r="10" fill="#fff" stroke="var(--icon)" stroke-width="3"/><path d="M51 46v6l4 3" stroke="var(--icon)" stroke-width="2" fill="none"/>
    </svg>STRATEGIC<br>PLANNING</div>

  <div class="service" style="left:360px">
    <svg class="service-icon" viewBox="0 0 78 78" aria-hidden="true">
      <circle cx="39" cy="39" r="33" fill="none" stroke="var(--ring)" stroke-width="9"/>
      <path d="M10 30A30 30 0 0 1 52 9" fill="none" stroke="var(--ring-green)" stroke-width="9"/>
      <circle cx="26" cy="22" r="6" fill="var(--icon)"/><rect x="19" y="30" width="13" height="24" rx="3" fill="var(--icon)"/>
      <circle cx="45" cy="48" r="13" fill="var(--icon)"/><circle cx="45" cy="48" r="9.5" fill="none" stroke="#fff" stroke-width="1.5"/>
      <text x="45" y="53" text-anchor="middle" font-family="Oxygen,sans-serif" font-weight="700" font-size="14" fill="#fff">$</text>
    </svg><span style="position:relative;top:-7px">HUMAN CAPITAL<br>MANAGEMENT SOLUTIONS</span></div>

  <div class="service" style="left:510px">
    <svg class="service-icon" viewBox="0 0 78 78" aria-hidden="true">
      <circle cx="39" cy="39" r="33" fill="none" stroke="var(--ring)" stroke-width="9"/>
      <path d="M10 30A30 30 0 0 1 52 9" fill="none" stroke="var(--ring-green)" stroke-width="9"/>
      <rect x="17" y="24" width="34" height="26" fill="#fff" stroke="var(--icon)" stroke-width="3"/>
      <path d="M21 43l7-8 6 5 7-9 6 5" stroke="var(--icon)" stroke-width="2.5" fill="none"/>
      <circle cx="50" cy="49" r="6" fill="#fff" stroke="var(--icon)" stroke-width="3"/><path d="M54 53l7 7" stroke="var(--icon)" stroke-width="4"/>
    </svg>FINANCIAL<br>ANALYSIS</div>

  <div class="service" style="left:646px">
    <svg class="service-icon" viewBox="0 0 78 78" aria-hidden="true">
      <circle cx="39" cy="39" r="33" fill="none" stroke="var(--ring)" stroke-width="9"/>
      <path d="M10 30A30 30 0 0 1 52 9" fill="none" stroke="var(--ring-green)" stroke-width="9"/>
      <path d="M32 27v-4h12v4" stroke="var(--icon)" stroke-width="3" fill="none"/>
      <rect x="18" y="27" width="40" height="25" rx="3" fill="var(--icon)"/><path d="M18 38h40" stroke="#fff" stroke-width="1.5"/><rect x="35" y="35" width="6" height="6" fill="#fff"/>
      <circle cx="56" cy="50" r="7" fill="#fff" stroke="var(--icon)" stroke-width="1.5"/>
      <text x="56" y="54" text-anchor="middle" font-family="Oxygen,sans-serif" font-weight="700" font-size="10" fill="var(--icon)">$</text>
    </svg>CASH MANAGEMENT<br>SOLUTIONS</div>
</section>

<section class="col" style="left:104px">
  <h3 class="col-title"><svg width="17" height="14" viewBox="0 0 17 14"><path d="M1 5h3l7-4v12L4 9H1z" fill="#333"/><path d="M13 4c1.5 1 1.5 5 0 6" stroke="#333" stroke-width="1.4" fill="none"/></svg><span><span class="accent">LATEST</span> NEWS</span></h3>
  <div class="news-item"><b>09/10/2014</b>Lorem ipsum dolor sit amet, cctetuer adipiscingin elit, sed diam nummy nibh eui smod tinciduntiot vulputate velit esse molestie</div>
  <div class="news-item"><b>10/10/2014</b>Lorem ipsum dolor sit amet, cctetuer adipiscingin elit, sed diam nummy nibh eui smod tinciduntiot vulputate velit esse molestie</div>
  <a class="read-more" href="#" style="margin-top:6px">Read more »</a>
</section>

<section class="col" style="left:337px">
  <h3 class="col-title"><svg width="17" height="14" viewBox="0 0 17 14"><rect x="0" y="0" width="11" height="8" rx="2" fill="#333"/><path d="M2 8v3l3-3z" fill="#333"/><rect x="6" y="5" width="11" height="7" rx="2" fill="#555"/></svg><span><span class="accent">CLIENT</span> TESTIMONIAL</span></h3>
  <div class="quote"><span class="quote-mark"></span>Duis autem vel eum iriureol hder in vultat velit esse moles conqat vela ilu dolor feugiat.Duis autem vel eum ure hendrern vultat velit esse autm vel eum iriure dol</div>
  <div class="client"><span class="client-photo" role="img" aria-label="Portrait photo of the client"></span><span class="client-name">Mr. Dolore Eu Feugiat</span></div>
  <a class="read-more" href="#" style="margin-top:-2px">Read more »</a>
</section>

<section class="col" style="left:571px">
  <h3 class="col-title"><svg width="15" height="14" viewBox="0 0 15 14"><rect x="1" y="2" width="10" height="11" fill="none" stroke="#333" stroke-width="1.4"/><path d="M6 9l7-7 1.5 1.5-7 7H6z" fill="#333"/></svg><span><span class="accent">QUICK</span> CONTACT</span></h3>
  <div style="margin-top:12px">
    <span class="field">Name</span>
    <span class="field">Email</span>
    <span class="field message">Message</span>
    <span class="submit" style="margin-left:-1px">Submit</span>
  </div>
</section>

<section class="clients">
  <h2 class="section-title"><span>OUR</span> <span class="accent">CLIENTS</span></h2>
  <span class="slider-arrow" style="left:82px;top:67px;width:22px;height:22px"><svg width="7" height="9" viewBox="0 0 8 10"><path d="M6 1 2 5l4 4" stroke="#fff" stroke-width="1.6" fill="none"/></svg></span>
  <div class="client-logo" style="left:117px;width:104px">Northwind</div>
  <div class="client-logo" style="left:231px;width:117px">Stonefield</div>
  <div class="client-logo" style="left:356px;width:140px"><i></i>Bluecrest</div>
  <div class="client-logo" style="left:517px;width:100px">Ardenwell</div>
  <div class="client-logo" style="left:637px;width:130px">Ledgerly</div>
  <span class="slider-arrow" style="left:779px;top:67px;width:22px;height:22px"><svg width="7" height="9" viewBox="0 0 8 10"><path d="M2 1l4 4-4 4" stroke="#fff" stroke-width="1.6" fill="none"/></svg></span>
</section>

<footer class="site-footer">
  <div class="footer-box" style="left:104px;width:180px">
    <h4>Subscribe to Newsletter</h4>
    <span class="newsletter-input">Email here</span><span class="newsletter-go"><svg width="8" height="10" viewBox="0 0 8 10"><path d="M2 1l4 4-4 4" stroke="#fff" stroke-width="2" fill="none"/></svg></span>
  </div>
  <div class="footer-box" style="left:305px;width:118px">
    <h4>Contact Us</h4>
    <div class="contact-line"><svg width="9" height="9" viewBox="0 0 14 14"><path d="M3 1c.6-.4 1.2-.3 1.5.2l1 1.8c.2.5 0 .9-.4 1.2l-.5.4c.6 1.4 1.6 2.4 3 3l.4-.5c.3-.4.7-.6 1.2-.4l1.8 1c.5.3.6.9.2 1.5-.8 1-2 1.3-3.2.8C5.4 8.8 4.2 7.6 3 5 2.5 3.6 2.4 2.3 3 1z" fill="#ccc"/></svg>555 014 2290</div>
    <div class="contact-line"><svg width="9" height="7" viewBox="0 0 10 7"><rect width="10" height="7" fill="#ccc"/><path d="M0 0l5 4 5-4" stroke="#333" fill="none"/></svg>info@veltrane.com</div>
  </div>
  <div class="footer-box" style="left:444px;width:87px">
    <h4>Follow Us</h4>
    <div class="social"><span aria-label="Social network one"></span><span aria-label="Social network two"></span><span aria-label="Social network three"></span></div>
  </div>
  <a class="brand" href="#"><span class="brand-mark"></span>Veltrane Management</a>
  <nav class="footer-links"><a href="#">Home</a> | <a href="#">About Us</a> | <a href="#">Services</a> | <a href="#">Contact Us</a> | <a href="#">Terms Conditions</a></nav>
  <p class="copyright">© 2014 &nbsp;Veltrane. All Rights Reserved</p>
</footer>

</body>
</html>
```